Wordpress Design Project - IT Consulting Services Web Site

Our are starting a new technology services company. We will provide services in software implementation and business intelligence.

We need a beautiful Wordpress web site design. We need a design for the homepage, and one interior content page.

The site must have a very professional and polished look and feel. What I have suggested below are things that I think work, but I am not a designer and I am open to your professional opinions. Please be willing to use your best judgment.

The homepage should have the following elements:
- A Header Area that includes:
o The company logo, and
o navigation (consistent with the interior page)
o a social media link section that includes rss feeds, youtube, facebook, linkedin and tweets
- A Body that includes:
o A slider
o An area that features up to six of the most recent or important posts including a thumbnail and small picture, a title, and a short excerpt for each.
o An area for around 100 words of text and an image
- A footer that includes:
o The company logo
o Contact information

The interior page is relatively simple. It should include the same navigation element as the homepage, and accommodate a one column text layout.

The current site …
You can visit the current site at www.korvelpath.com I built the current site using the “Velthor Quick Pane” premium theme. If you visit this site you get a sense of some of the things I am talking about, but there are things that I do not like about the current site. Here’s what I like and what I don’t like.

What I like about the current site:
- It is reactive – it adapts to the size of the viewing browser
- It has a “metro” feel to it. The company will have an association with Microsoft and having a “metro” theme is a plus, but not a requirement.
- It is different without being hard to navigate – the site the slider is from the “glide cascade widget”, the posts are represented with tiles and rearrange themselves when a topic is selected.

What I don’t like:
- The site lacks a cohesive feel – it feels to me like a bunch of different elements without a single theme that pulls everything together.
- It is not aesthetically appealing to me.
- The tiles in the post section are too big.
- I don’t like the white background – I would prefer a background color and ideally a background that somehow incorporates the graphic in the logo.

About themes
As I said, I used a Velthor theme in my design. I will be happy to continue using this theme, or would be willing to buy a new premium theme, so long as the cost is less than $100 U.S.

Site Map:
What we do
ERP Implementation
Business Intelligence
Who we are
What’s different about us
Principles
Mission, Vision, Values
Actions
How we work
What’s Different About Us
Blogs
What Papers
Presentations
Join
What we are looking for
What are you looking for?
Benefits
Context
Updates

Regarding Pictures
Please do not feel you need to use any of the pictures currently on the site.  Use whatever pictures you feel look best.  Comps are okay. 

It is not necessary to use any of the content on the current site - you do not need to use either the pictures or the text.  Please feel free to use pictures of your choice (comps okay), and/or lorem text.

The top level navigation is the navigation I would like.

Hello all,

Since this is a Wordpress project, it goes without saying I will need to implement this design in Wordpress.  It is not absolutely necessary that a design that matches an existing template (free or not), but a design that does will have an advantage over a design which requires that a new template be coded from scratch.

Thank you.

Target Market(s)

Business executives and potential employees

Industry/Entity Type

Software

Requirements
Nice to have
• It would be nice if the site was reactive.

```html
<!DOCTYPE html>
<html lang="en">
<head>
<meta charset="utf-8">
<title>Korvel Path — Home</title>
<link href="https://fonts.googleapis.com/css2?family=PT+Sans:wght@400;700&family=Yanone+Kaffeesatz:wght@300;400;600&display=swap" rel="stylesheet">
<style>
:root{
  --bg-dark:#1f1f1f;
  --bg-mid:#2c2c2c;
  --panel:#4a4a4a;
  --panel-edge:#5c5c5c;
  --rule:#6a6a6a;
  --text-light:#e6e6e6;
  --text-soft:#d0d0d0;
  --accent:#1e9fe0;
  --accent-deep:#0b7dbd;
  --footer-top:#0a8ccc;
  --footer-bottom:#0b6a9f;
  --frame:#f1f1f1;
  --social:#5a5a5a;
}
*{box-sizing:border-box;margin:0;padding:0}
html,body{width:1109px;height:1200px;overflow:hidden}
body{
  position:relative;
  font-family:"PT Sans",sans-serif;
  color:var(--text-light);
  background:
    repeating-linear-gradient(90deg,rgba(255,255,255,.018) 0 3px,rgba(0,0,0,.03) 3px 9px,rgba(255,255,255,.01) 9px 17px),
    linear-gradient(180deg,var(--bg-mid),var(--bg-dark));
}
.abs{position:absolute}

/* header */
.brand{left:120px;top:70px;display:flex;align-items:center;gap:10px}
.brand-name{font-size:31px;color:#c9c9c9;letter-spacing:-.5px}
.brand-dot{width:14px;height:14px;border-radius:50%;background:var(--accent)}
.social{left:793px;top:29px;display:flex;gap:10px}
.social a{display:block;width:25px;height:25px;background:var(--social);border-radius:3px}
.nav{left:548px;top:73px;height:47px;display:flex;align-items:flex-end}
.nav a{display:block;color:#fff;text-decoration:none;font-size:12.5px;letter-spacing:.3px;padding:0 10px 13px}
.nav a.active{background:var(--accent-deep);border-radius:4px 4px 0 0;padding:20px 10px 13px}

/* slider */
.slider{left:113px;top:120px;width:887px;height:306px;background:var(--frame);border-radius:3px}
.slide{position:absolute;left:8px;top:9px;width:872px;height:288px;border-radius:3px;
  background:linear-gradient(180deg,#4f86b8 0%,#6e9dc8 55%,#8cb3d6 100%)}
.slide-title{left:95px;top:88px;font-family:"Yanone Kaffeesatz",sans-serif;font-weight:400;font-size:23px;color:#fff;
  padding-bottom:4px;border-bottom:1px solid rgba(255,255,255,.45);width:311px;white-space:nowrap}
.slide-text{left:95px;top:125px;width:320px;font-size:12px;line-height:19.4px;color:#fff}
.pager{left:386px;top:270px;width:116px;height:28px;background:var(--frame);border-radius:6px 6px 0 0;
  display:flex;justify-content:center;align-items:center;gap:14px}
.pager i{width:11px;height:11px;border-radius:50%;background:#9a9a9a}
.pager i.on{background:#3f7fb5}

/* posts */
.panel{left:113px;top:462px;width:886px;height:541px;background:var(--panel);border:1px solid var(--panel-edge);border-radius:3px}
.panel-title{left:30px;top:22px;font-family:"Yanone Kaffeesatz",sans-serif;font-weight:600;font-size:21px;color:#fff;letter-spacing:.2px}
.rule{left:30px;width:812px;height:2px;background:var(--rule)}
.post{width:270px;height:70px}
.post-thumb{position:absolute;left:0;top:0;width:94px;height:69px;border:3px solid #e9e9e9}
.post-title{position:absolute;left:103px;top:-1px;font-family:"Yanone Kaffeesatz",sans-serif;font-size:13px;color:#fff;white-space:nowrap}
.post-text{position:absolute;left:103px;top:17px;width:130px;font-size:11px;line-height:13px;color:var(--text-soft);text-align:justify}
.more{left:800px;top:260px;font-size:12px;color:#fff}
.feature-img{left:27px;top:319px;width:186px;height:185px;border-radius:3px;background:linear-gradient(135deg,#b9c4cc,#6b7580 60%,#3b4047)}
.feature{left:232px;width:616px}
.feature small{display:block;font-size:11px;color:var(--text-soft)}
.feature h3{font-weight:400;font-size:15px;color:var(--accent);margin:1px 0 5px}
.feature p{font-size:10.6px;line-height:13px;color:var(--text-soft)}

/* footer */
.footer{left:0;top:1036px;width:1109px;height:164px;background:linear-gradient(180deg,var(--footer-top),var(--footer-bottom))}
.foot-col h4{font-weight:400;font-size:17px;color:#fff;margin-bottom:12px}
.foot-col p{font-size:11px;line-height:16.6px;color:#e8f3fa}
.foot-brand{left:801px;top:40px;display:flex;align-items:center;gap:9px}
.foot-brand .brand-name{font-size:24px;color:#3a3a3a}
.foot-brand .brand-dot{width:11px;height:11px;background:#3a3a3a}
.copy{right:124px;top:113px;font-size:11px;color:#e8f3fa}
</style>
</head>
<body>

<header>
  <div class="abs brand"><span class="brand-name">Korvel Path</span><span class="brand-dot"></span></div>
  <nav class="abs social" aria-label="Social links">
    <a href="#" aria-label="Social link 1"></a><a href="#" aria-label="Social link 2"></a><a href="#" aria-label="Social link 3"></a>
    <a href="#" aria-label="RSS"></a><a href="#" aria-label="Video channel"></a><a href="#" aria-label="Photo channel"></a>
  </nav>
  <nav class="abs nav">
    <a href="#" class="active">WHAT WE DO</a><a href="#">WHO WE ARE</a><a href="#">HOW WE WORK</a><a href="#">JOIN US</a><a href="#">CONTACT US</a>
  </nav>
</header>

<section class="abs slider">
  <div class="slide" role="img" aria-label="Slide photo: woman with raised arms against a blue sky">
    <h2 class="abs slide-title">LOREM IPSUM DOLOR SIT AMET, ELIT</h2>
    <p class="abs slide-text">Cum sociis natoque penatibus et magnis dis parturient montes, nascetur ridiculus mus. In iaculis facilisis massa. Etiam eu urna. Sed porta.Cum sociis natoque penatibus et magnis dis parturient montes, nascetur ridiculus mus. In iaculis facilisis massa. Etiam eu urna. Sed porta.</p>
  </div>
  <div class="abs pager"><i></i><i></i><i class="on"></i><i></i></div>
</section>

<main class="abs panel">
  <h2 class="abs panel-title">MOST RECENT POSTS</h2>
  <div class="abs rule" style="top:48px"></div>

  <article class="abs post" style="left:30px;top:65px"><div class="post-thumb" role="img" aria-label="Photo: business team at a desk" style="background:linear-gradient(135deg,#dfe6ee,#8a96a6)"></div><h3 class="post-title">SED UT PERSPICIATIS UNDE OMNIS</h3><p class="post-text">Sed ut perspiciatis unde omnis iste natus error sit voluptatem accusantium aperiam, eaque quae ab</p></article>
  <article class="abs post" style="left:318px;top:65px"><div class="post-thumb" role="img" aria-label="Photo: pens on technical plans" style="background:linear-gradient(135deg,#f2f2f2,#b7bcc4)"></div><h3 class="post-title">SED UT PERSPICIATIS UNDE OMNIS</h3><p class="post-text">Sed ut perspiciatis unde omnis iste natus error sit voluptatem accusantium aperiam, eaque quae ab</p></article>
  <article class="abs post" style="left:605px;top:65px"><div class="post-thumb" role="img" aria-label="Photo: three colleagues in an office" style="background:linear-gradient(135deg,#8c8a7e,#4a4a44)"></div><h3 class="post-title">SED UT PERSPICIATIS UNDE OMNIS</h3><p class="post-text">Sed ut perspiciatis unde omnis iste natus error sit voluptatem accusantium aperiam, eaque quae ab</p></article>
  <article class="abs post" style="left:30px;top:167px"><div class="post-thumb" role="img" aria-label="Photo: hands typing on a keyboard" style="background:linear-gradient(135deg,#efe8e4,#b9b2ae)"></div><h3 class="post-title">SED UT PERSPICIATIS UNDE OMNIS</h3><p class="post-text">Sed ut perspiciatis unde omnis iste natus error sit voluptatem accusantium aperiam, eaque quae ab</p></article>
  <article class="abs post" style="left:318px;top:167px"><div class="post-thumb" role="img" aria-label="Illustration: handshake with puzzle pieces" style="background:linear-gradient(180deg,#7fc0e6,#f4f4f4 70%)"></div><h3 class="post-title">SED UT PERSPICIATIS UNDE OMNIS</h3><p class="post-text">Sed ut perspiciatis unde omnis iste natus error sit voluptatem accusantium aperiam, eaque quae ab</p></article>
  <article class="abs post" style="left:605px;top:167px"><div class="post-thumb" role="img" aria-label="Photo: students working at computers" style="background:linear-gradient(135deg,#6e6a66,#3a3836)"></div><h3 class="post-title">SED UT PERSPICIATIS UNDE OMNIS</h3><p class="post-text">Sed ut perspiciatis unde omnis iste natus error sit voluptatem accusantium aperiam, eaque quae ab</p></article>

  <a class="abs more">More &gt;&gt;</a>
  <div class="abs rule" style="top:289px"></div>

  <div class="abs feature-img" role="img" aria-label="Photo: business people in a meeting"></div>
  <div class="abs feature" style="top:324px">
    <small>People, Processes and Tools</small>
    <h3>Putting People First</h3>
    <p>Every services firm is made up of people, processes and tools. At Korvel Path, we put people first, tailoring everything we do to find, hire, train, and keep the very best people. Because once you have the best people everything else follows.</p>
  </div>
  <div class="abs feature" style="top:427px">
    <small>Korvel Path</small>
    <h3>What's the idea?</h3>
    <p>The idea is an old one but a great one.  Edmund Harlow Price was an American writer credited with creating the phrase "The American Dream". It's the idea that your success should depend on your ability and achievements, not on where you started out.  It's an idea we try to live up to.</p>
  </div>
</main>

<footer class="abs footer">
  <div class="abs foot-col" style="left:112px;top:22px;width:310px">
    <h4>About Korvel Path</h4>
    <p>Korvel Path provides technology services in a variety of areas. What makes us different is our focus on finding, training and retaining the very best people, who focus on providing our customers with the very best service.</p>
  </div>
  <div class="abs foot-col" style="left:510px;top:22px;width:260px">
    <h4>Contact Information</h4>
    <p style="padding-left:3px">418 Harrowfield Pkwy, Elmstead, MN<br><br>Phone :  555 014 227<br>Email : info@korvelpath.com</p>
  </div>
  <div class="abs foot-brand"><span class="brand-name">Korvel Path</span><span class="brand-dot"></span></div>
  <p class="abs copy">© 2013 korvelpath, All Rights Reserved</p>
</footer>

</body>
</html>
```